Tobias Wrenfeld and Co stationary design

Name of business:
Tobias Wrenfeld and Co

Can be written as:
Tobias Wrenfeld and Co
Tobias Wrenfeld & Co
tobias wrenfeld & co

If broken into letters:
TW&Co
tw&co

We are a Railway Safety Training Company
Our focus is on rail safety, Rail Management, Safety Management, Train Control Training, Accident Investigation.

.

Project Deadline Extended Reason: The original date was set to commence as soon as the logo contest finished. Sketch guild started the project as soon as it was paid. Added Thursday, May 12, 2016

Target Market(s)

Professionals, CEO's and Managing Directors

Industry/Entity Type

Management Consulting

Font styles to use
Sans Serif

Requirements
Must have
• Professional, Sharp, Creative and modern
• Please note that this is for stationary concept which must include
• - business card
• - letterhead
• - envelope
• - with compliments slip
• - document cover (like book or folder cover)
• - dividers for folders....
• These must all have a common theme or style
Nice to have
• Keep if fresh
Should not have
• Please don't sent just fonts.... Must be creative

```html
<!DOCTYPE html>
<html lang="en">
<head>
<meta charset="utf-8">
<title>Tobias Wrenfeld &amp; Co — Business Card</title>
<link href="https://fonts.googleapis.com/css2?family=Roboto+Condensed:wght@400;700&display=swap" rel="stylesheet">
<style>
  :root {
    --navy: #1e3468;
    --navy-deep: #172a57;
    --navy-faint: #2a4279;
    --red: #d4203a;
    --white: #ffffff;
    --ink: #1e3468;
    --stage: #e9eaee;
  }
  * { margin: 0; padding: 0; box-sizing: border-box; }
  html, body { width: 1200px; height: 950px; overflow: hidden; }
  body {
    background: var(--stage);
    font-family: "Roboto Condensed", "Arial Narrow", sans-serif;
    display: flex; flex-direction: column; align-items: center; justify-content: center;
    gap: 40px;
  }
  .card {
    position: relative; width: 740px; height: 420px;
    border-radius: 22px; overflow: hidden;
    box-shadow: 0 6px 18px rgba(20, 30, 60, .18);
  }
  .card-bg { position: absolute; inset: 0; width: 100%; height: 100%; }

  /* Front */
  .card--front { background: var(--white); }
  .brand { position: absolute; left: 110px; top: 168px; display: flex; align-items: center; gap: 14px; }
  .brand-dot { width: 64px; height: 64px; border-radius: 50%; background: var(--navy); }
  .brand-name { font-size: 44px; font-weight: 700; color: var(--navy); letter-spacing: .5px; }
  .person { position: absolute; left: 56px; bottom: 56px; }
  .person-name { font-size: 28px; font-weight: 700; color: var(--navy); letter-spacing: 1px; text-transform: uppercase; }
  .person-title { font-size: 20px; color: var(--red); text-transform: uppercase; letter-spacing: 1px; }

  .contacts { position: absolute; right: 36px; top: 48px; list-style: none; text-align: right; }
  .contacts li { display: flex; justify-content: flex-end; align-items: center; gap: 12px;
    font-size: 21px; color: var(--white); line-height: 36px; }
  .contacts svg { width: 18px; height: 18px; fill: var(--red); }
  .address { position: absolute; right: 36px; bottom: 40px; display: flex; align-items: center; gap: 12px;
    font-size: 21px; color: var(--white); }
  .address svg { width: 18px; height: 18px; fill: var(--red); }

  /* Back */
  .card--back { background: var(--navy); }
  .back-title { position: absolute; left: 0; right: 0; top: 160px; text-align: center;
    font-size: 50px; font-weight: 700; color: var(--white); letter-spacing: 1px; }
  .back-web { position: absolute; left: 0; right: 0; top: 236px; text-align: center;
    font-size: 20px; color: var(--white); letter-spacing: 9px; }
</style>
</head>
<body>

  <section class="card card--front" aria-label="Business card front">
    <svg class="card-bg" viewBox="0 0 740 420" preserveAspectRatio="none" aria-hidden="true">
      <path d="M478 0 C410 150 380 300 262 420 L740 420 L740 0 Z" fill="var(--navy)"/>
      <path d="M446 0 C392 110 368 190 332 262 C382 192 414 110 470 0 Z" fill="var(--red)"/>
    </svg>

    <div class="brand">
      <span class="brand-dot"></span>
      <span class="brand-name">TW &amp; Co.</span>
    </div>

    <div class="person">
      <p class="person-name">Mara Ellison</p>
      <p class="person-title">CEO/Founder</p>
    </div>

    <ul class="contacts">
      <li>555 014 2291
        <svg viewBox="0 0 24 24"><path d="M6.6 10.8a15 15 0 0 0 6.6 6.6l2.2-2.2a1 1 0 0 1 1-.25 11.4 11.4 0 0 0 3.6.57 1 1 0 0 1 1 1V20a1 1 0 0 1-1 1A17 17 0 0 1 3 4a1 1 0 0 1 1-1h3.5a1 1 0 0 1 1 1c0 1.25.2 2.45.57 3.57a1 1 0 0 1-.25 1z"/></svg>
      </li>
      <li>555 017 8830
        <svg viewBox="0 0 24 24"><rect x="3" y="7" width="18" height="12" rx="2"/><rect x="7" y="3" width="10" height="5"/></svg>
      </li>
      <li>555 019 4475
        <svg viewBox="0 0 24 24"><rect x="6" y="2" width="12" height="20" rx="2"/></svg>
      </li>
      <li>hello@wrenfeldco.com
        <svg viewBox="0 0 24 24"><path d="M2 5h20v14H2z M2 5l10 8 10-8" stroke="#fff" stroke-width="1.2"/></svg>
      </li>
      <li>www.wrenfeldco.com
        <svg viewBox="0 0 24 24"><circle cx="12" cy="12" r="10"/></svg>
      </li>
    </ul>

    <p class="address">1420 Harbor Row, Fairview, Oregon 97024
      <svg viewBox="0 0 24 24"><path d="M12 2a7 7 0 0 0-7 7c0 5 7 13 7 13s7-8 7-13a7 7 0 0 0-7-7zm0 9.5A2.5 2.5 0 1 1 12 6.5a2.5 2.5 0 0 1 0 5z"/></svg>
    </p>
  </section>

  <section class="card card--back" aria-label="Business card back">
    <p class="back-title">Tobias Wrenfeld &amp; Co.</p>
    <p class="back-web">www.wrenfeldco.com</p>
  </section>

</body>
</html>
```